Korvane Supplies Ltd Stationery Design Project

hi we need to design business cards, letter head, complimentary slips, scribble pads, note pads, envelopes for korvane supplies ltd.

please see business cards details

Tobias Welkerin

P.O Box 41823 -00719 Nairobi - Kenya
Tel: +254-733-182-947
Email: korvanesupplies@brelomail.test

company name should appear on all stationery : Korvane Supplies Ltd

Industry/Entity Type

Business

Requirements
Must have
• kindly stick to colours in the logo

```html
<!DOCTYPE html>
<html lang="en">
<head>
<meta charset="utf-8">
<title>Korvane Supplies Ltd — Stationery Set</title>
<link rel="stylesheet" href="https://fonts.googleapis.com/css2?family=Open+Sans:wght@400;600;700&display=swap">
<style>
  :root {
    --bg: #e9eaec;
    --paper: #ffffff;
    --orange: #f29a1e;
    --orange-deep: #ea6a12;
    --yellow: #f6c445;
    --blue: #2b4c9b;
    --ink: #222222;
    --label: #555555;
    --rule: #c9c9c9;
    --ghost: #ededed;
  }
  * { margin: 0; padding: 0; box-sizing: border-box; }
  html, body { width: 1200px; height: 775px; overflow: hidden; }
  body {
    position: relative;
    background: var(--bg);
    font-family: "Open Sans", Arial, sans-serif;
    color: var(--ink);
  }
  .item-label {
    position: absolute;
    font-size: 7px;
    letter-spacing: 0.4px;
    color: var(--label);
    text-transform: uppercase;
  }
  .sheet { position: absolute; background: var(--paper); overflow: hidden; }

  .brand-name {
    font-family: "Open Sans", Arial, sans-serif;
    font-weight: 700;
    color: var(--orange);
    text-transform: uppercase;
    line-height: 1;
    text-align: center;
    letter-spacing: 0.5px;
  }
  .brand-name .line { display: block; }
  .brand-dot {
    display: block;
    margin: 0 auto 3px;
    border-radius: 50%;
    background: var(--orange);
  }

  .sun-ornament { position: absolute; border-radius: 50% 50% 0 0; }
  .sun-ornament.faint { background: radial-gradient(circle at 50% 100%, #e4e4e4 0%, #efefef 45%, rgba(255,255,255,0) 72%); }

  /* Letterhead */
  .letterhead { left: 150px; top: 97px; width: 285px; height: 405px; }
  .letterhead .brand { position: absolute; left: 0; width: 100%; top: 14px; }
  .letterhead .brand-name { font-size: 15px; }
  .letter-body { position: absolute; left: 30px; top: 88px; width: 228px; font-size: 3.6px; line-height: 5.2px; }
  .letter-body p { margin-bottom: 5px; }
  .letter-body .date, .letter-body .greeting { font-weight: 600; }
  .signature-mark { width: 34px; height: 10px; margin: 3px 0 2px; background: linear-gradient(90deg, rgba(43,76,155,0.35), rgba(43,76,155,0.1)); border-radius: 3px; }
  .signer { font-weight: 700; }
  .letterhead .sun-ornament { left: 40px; top: 300px; width: 220px; height: 190px; }
  .sheet-footer { position: absolute; left: 0; right: 0; bottom: 0; }
  .letterhead .contact-line {
    position: absolute; left: 0; right: 0; bottom: 16px;
    display: flex; justify-content: center; gap: 10px;
    font-size: 3.4px; color: var(--blue);
  }
  .contact-line span::before { content: ""; display: inline-block; width: 2.5px; height: 2.5px; background: var(--orange); border-radius: 50%; margin-right: 2px; vertical-align: middle; }
  .orange-band {
    position: absolute; left: 0; right: 0; bottom: 0; height: 12px;
    background: linear-gradient(90deg, var(--orange) 0%, var(--yellow) 50%, var(--orange) 100%);
    display: flex; align-items: center; justify-content: center;
  }
  .band-name { font-size: 3.4px; color: var(--blue); font-weight: 600; }

  /* Folder */
  .folder { left: 487px; top: 77px; width: 337px; height: 427px; background: linear-gradient(200deg, var(--yellow) 0%, var(--orange) 45%, #f0831a 100%); }
  .folder .brand { position: absolute; left: 0; width: 100%; top: 90px; }
  .folder .brand-name { color: #ffffff; font-size: 30px; letter-spacing: 1px; }
  .folder .brand-name .line + .line { font-size: 20px; margin-top: 3px; }
  .folder .brand-dot { background: #ffffff; width: 12px; height: 12px; margin-bottom: 8px; }
  .folder .sun-ornament { left: -10px; top: 215px; width: 357px; height: 212px; background: radial-gradient(circle at 50% 100%, var(--orange-deep) 0%, #ef7a17 40%, rgba(240,131,26,0) 72%); }
  .folder .web { position: absolute; left: 0; right: 0; bottom: 16px; text-align: center; font-size: 8px; color: #ffffff; }

  /* Notepad */
  .notepad { left: 876px; top: 175px; width: 224px; height: 325px; }
  .spiral { position: absolute; left: 876px; top: 160px; width: 224px; height: 22px; }
  .notepad .brand { position: absolute; left: 0; width: 100%; top: 26px; }
  .notepad .brand-name { font-size: 10px; }
  .notepad .date-field { position: absolute; left: 12px; top: 66px; font-size: 5px; color: var(--blue); }
  .ruled-lines { position: absolute; left: 12px; right: 16px; top: 84px; height: 212px;
    background: repeating-linear-gradient(to bottom, transparent 0, transparent 10px, var(--rule) 10px, var(--rule) 10.6px); }
  .notepad .sun-ornament { left: 22px; top: 222px; width: 180px; height: 100px; }
  .notepad .orange-band { height: 8px; }

  /* Business cards */
  .card-front { left: 47px; top: 537px; width: 130px; height: 73px; }
  .card-front .holder { position: absolute; left: 9px; top: 12px; font-size: 5.5px; color: var(--blue); font-weight: 600; text-transform: uppercase; }
  .card-front .role { position: absolute; left: 9px; top: 19px; font-size: 3.6px; color: var(--orange); }
  .card-front .details { position: absolute; left: 9px; top: 28px; font-size: 3.2px; line-height: 4.4px; color: var(--blue); }
  .card-front .brand { position: absolute; right: 8px; top: 28px; }
  .card-front .brand-name { font-size: 8.5px; }
  .card-back { left: 47px; top: 630px; width: 130px; height: 73px; background: radial-gradient(circle at 50% 50%, var(--yellow) 0%, var(--orange) 60%, #f08a1c 100%); display: flex; align-items: center; justify-content: center; }
  .card-back .band-name { font-size: 3.6px; }

  /* Envelopes */
  .envelope-front { left: 210px; top: 548px; width: 320px; height: 152px; }
  .envelope-front .brand { position: absolute; left: 12px; top: 14px; }
  .envelope-front .brand-name { font-size: 13px; text-align: left; }
  .envelope-front .address { position: absolute; left: 13px; bottom: 12px; font-size: 4px; line-height: 5.4px; color: var(--blue); }
  .envelope-front .address .company { color: var(--orange); font-weight: 600; }
  .envelope-back { left: 561px; top: 548px; width: 320px; height: 152px; }
  .envelope-flap { position: absolute; left: 0; top: 0; width: 320px; height: 62px; }
  .envelope-flap .band-name { position: absolute; left: 0; right: 0; top: 22px; text-align: center; font-size: 4px; }
  .envelope-back .sun-ornament { left: 60px; top: 40px; width: 200px; height: 112px; }

  /* Compliment slip */
  .compliment-slip { left: 914px; top: 575px; width: 242px; height: 122px; }
  .compliment-slip .brand { position: absolute; left: 6px; top: 10px; }
  .compliment-slip .brand-name { font-size: 9px; text-align: left; }
  .compliment-slip .details { position: absolute; left: 7px; top: 34px; font-size: 3px; line-height: 4px; color: var(--blue); }
  .compliment-slip .with-compliments { position: absolute; left: 7px; bottom: 6px; font-size: 5.5px; font-style: italic; color: var(--blue); }
  .compliment-slip .sun-ornament { left: 130px; top: 20px; width: 100px; height: 100px; }
  .slip-band { position: absolute; right: 0; top: 0; width: 46px; height: 100%; background: linear-gradient(180deg, var(--orange) 0%, var(--yellow) 50%, var(--orange) 100%); display: flex; align-items: center; justify-content: center; }
  .slip-band .band-name { font-size: 3.4px; }
</style>
</head>
<body>

  <span class="item-label" style="left:150px; top:72px;">Letterhead</span>
  <span class="item-label" style="left:620px; top:52px;">A4 Folder Cover</span>
  <span class="item-label" style="left:1068px; top:139px;">Notepad</span>
  <span class="item-label" style="left:47px; top:716px;">Business Card</span>
  <span class="item-label" style="left:527px; top:716px;">Envelope</span>
  <span class="item-label" style="left:1078px; top:716px;">Complimentary Slips</span>

  <!-- Letterhead -->
  <section class="sheet letterhead">
    <div class="sun-ornament faint" role="img" aria-label="Faint decorative sun ornament"></div>
    <div class="brand">
      <span class="brand-dot" style="width:8px;height:8px;"></span>
      <p class="brand-name"><span class="line">Korvane</span><span class="line" style="font-size:10px;margin-top:1px;">Supplies</span></p>
    </div>
    <div class="letter-body">
      <p class="date">Date: July, 19th 2013</p>
      <p class="greeting">Dear Customer,</p>
      <p>Thank you for choosing us as your trusted partner for office supplies. We stock paper, files, pens, toner and printing materials for businesses of every size, and we deliver across the city within two working days of your order.</p>
      <p>Our team is ready to help you plan your monthly stationery needs and keep your office running smoothly. Please find attached our latest price list together with details of the new bulk discounts available this quarter.</p>
      <p>Orders can be placed by phone or email at any time, and our account managers will confirm stock and delivery dates on the same day. Regular customers may also open a credit account with simple monthly billing.</p>
      <p>We look forward to serving you and building a lasting relationship with your business. Should you have any questions, do not hesitate to contact our office.</p>
      <p>Regards,</p>
      <div class="signature-mark" role="img" aria-label="Handwritten signature"></div>
      <p class="signer" style="margin-bottom:0;">TOBIAS WELKERIN</p>
      <p>Director</p>
    </div>
    <div class="contact-line">
      <span>P.O Box 41823 -00719 Nairobi - Kenya</span>
      <span>+254-733-182-947</span>
      <span>korvanesupplies@brelomail.test</span>
    </div>
    <div class="orange-band"><span class="band-name">Korvane Supplies Ltd</span></div>
  </section>

  <!-- Folder cover -->
  <section class="sheet folder">
    <div class="sun-ornament" role="img" aria-label="Large decorative rising sun with swirling rays"></div>
    <div class="brand">
      <span class="brand-dot"></span>
      <p class="brand-name"><span class="line">Korvane</span><span class="line">Supplies</span></p>
    </div>
    <p class="web">www.KorvaneSupplies.test</p>
  </section>

  <!-- Notepad -->
  <section class="sheet notepad">
    <div class="sun-ornament faint" role="img" aria-label="Faint decorative sun ornament"></div>
    <div class="brand">
      <span class="brand-dot" style="width:6px;height:6px;"></span>
      <p class="brand-name"><span class="line">Korvane</span><span class="line" style="font-size:7px;margin-top:1px;">Supplies</span></p>
    </div>
    <p class="date-field">Date: __________</p>
    <div class="ruled-lines"></div>
    <div class="orange-band"><span class="band-name">Korvane Supplies</span></div>
  </section>
  <svg class="spiral" viewBox="0 0 224 22" aria-hidden="true">
    <g fill="none" stroke="#333" stroke-width="1.3">
      <path d="M8 20 V6 a3 3 0 0 1 6 0 V20"/><path d="M22 20 V6 a3 3 0 0 1 6 0 V20"/><path d="M36 20 V6 a3 3 0 0 1 6 0 V20"/><path d="M50 20 V6 a3 3 0 0 1 6 0 V20"/><path d="M64 20 V6 a3 3 0 0 1 6 0 V20"/><path d="M78 20 V6 a3 3 0 0 1 6 0 V20"/><path d="M92 20 V6 a3 3 0 0 1 6 0 V20"/><path d="M106 20 V6 a3 3 0 0 1 6 0 V20"/><path d="M120 20 V6 a3 3 0 0 1 6 0 V20"/><path d="M134 20 V6 a3 3 0 0 1 6 0 V20"/><path d="M148 20 V6 a3 3 0 0 1 6 0 V20"/><path d="M162 20 V6 a3 3 0 0 1 6 0 V20"/><path d="M176 20 V6 a3 3 0 0 1 6 0 V20"/><path d="M190 20 V6 a3 3 0 0 1 6 0 V20"/><path d="M204 20 V6 a3 3 0 0 1 6 0 V20"/>
    </g>
  </svg>

  <!-- Business card -->
  <section class="sheet card-front">
    <p class="holder">Tobias Welkerin</p>
    <p class="role">Director</p>
    <p class="details">Korvane Supplies Ltd<br>P.O Box 41823 -00719<br>Nairobi - Kenya<br>+254-733-182-947<br>korvanesupplies@brelomail.test</p>
    <div class="brand">
      <span class="brand-dot" style="width:5px;height:5px;"></span>
      <p class="brand-name"><span class="line">Korvane</span><span class="line" style="font-size:6px;margin-top:1px;">Supplies</span></p>
    </div>
  </section>
  <section class="sheet card-back" role="img" aria-label="Orange card back with decorative sun ornament">
    <span class="band-name">Korvane Supplies</span>
  </section>

  <!-- Envelope front -->
  <section class="sheet envelope-front">
    <div class="brand">
      <p class="brand-name"><span class="line">Korvane</span><span class="line" style="font-size:9px;margin-top:1px;">Supplies</span></p>
    </div>
    <p class="address"><span class="company">Korvane Supplies Ltd.</span><br>P.O Box 41823 -00719 Nairobi - Kenya<br>+254-733-182-947 &nbsp; korvanesupplies@brelomail.test</p>
  </section>

  <!-- Envelope back -->
  <section class="sheet envelope-back">
    <div class="sun-ornament faint" role="img" aria-label="Faint decorative sun ornament"></div>
    <svg class="envelope-flap" viewBox="0 0 320 62" role="img" aria-label="Orange envelope flap with sun ornament">
      <defs>
        <radialGradient id="flapGlow" cx="50%" cy="30%" r="60%">
          <stop offset="0" stop-color="#f6c445"/>
          <stop offset="1" stop-color="#f29a1e"/>
        </radialGradient>
      </defs>
      <path d="M0 0 H320 L312 56 Q160 66 8 56 Z" fill="url(#flapGlow)"/>
    </svg>
    <div class="envelope-flap"><span class="band-name">Korvane Supplies</span></div>
  </section>

  <!-- Compliment slip -->
  <section class="sheet compliment-slip">
    <div class="sun-ornament faint" role="img" aria-label="Faint decorative sun ornament"></div>
    <div class="brand">
      <span class="brand-dot" style="width:5px;height:5px;margin-left:0;"></span>
      <p class="brand-name"><span class="line">Korvane</span><span class="line" style="font-size:6.5px;margin-top:1px;">Supplies</span></p>
    </div>
    <p class="details">Korvane Supplies Ltd<br>P.O Box 41823 -00719<br>+254-733-182-947<br>korvanesupplies@brelomail.test</p>
    <p class="with-compliments">With compliments</p>
    <div class="slip-band"><span class="band-name">Korvane Supplies</span></div>
  </section>

</body>
</html>
```